Business Card Design Project

Corwen Property Management

Our Business is residential property management, we therefore need a card that displays a professional image, but is clear and concise, and easy to read
Updates

We are committed now guys and girls, loving what we are seeing so far! 

Target Market(s)

Landlords, Rental Property Owners

Industry/Entity Type

Residential

Requirements
Must have
• Dean Fosterly - Principal
Tessa Fosterly - Director (Property Management)

PO Box 718
Holloway SA 5093

Dean: 0419 372 508
Tessa: 0419 613 947

www.corwenpropertymanagement.com.au
admin@corwenpropertymanagement.com.au

Nice to have
• I would like the card to be double sided, white background on the information side and then colour on the reverse, in blue or black and incorporating our logo

```html
<!DOCTYPE html>
<html lang="en">
<head>
<meta charset="utf-8">
<title>Corwen Property Management – Business Card</title>
<link rel="stylesheet" href="https://fonts.googleapis.com/css2?family=Open+Sans:wght@400;600;700&display=swap">
<style>
  :root {
    --stage: #1f1f1f;
    --card: #ffffff;
    --ink: #333333;
    --detail: #4a4a4a;
    --accent: #1a8cf0;
    --accent-deep: #0a5fd0;
    --rule: #1aa3f0;
  }
  * { margin: 0; padding: 0; box-sizing: border-box; }
  html, body {
    width: 1200px;
    height: 900px;
    overflow: hidden;
  }
  body {
    position: relative;
    background: var(--stage);
    font-family: "Open Sans", Arial, sans-serif;
  }
  .card {
    position: absolute;
    background: var(--card);
    border-radius: 12px;
  }
  .card--front { left: 162px; top: 73px; width: 716px; height: 418px; }
  .card--back  { left: 422px; top: 468px; width: 678px; height: 396px; }

  .brand {
    position: absolute;
    display: flex;
    align-items: center;
    gap: 14px;
  }
  .brand__mark {
    flex: none;
    background: linear-gradient(180deg, var(--accent), var(--accent-deep));
  }
  .brand__name {
    display: flex;
    flex-direction: column;
    color: var(--ink);
    font-weight: 600;
    white-space: nowrap;
  }
  .brand__word { line-height: 1; }
  .brand__line { line-height: 1.1; }

  .card--front .brand { left: 34px; top: 184px; }
  .card--front .brand__mark { width: 70px; height: 66px; }
  .card--front .brand__word { font-size: 46px; }
  .card--front .brand__line { font-size: 14.5px; padding-left: 2px; }

  .card--back .brand { left: 144px; top: 152px; }
  .card--back .brand__mark { width: 100px; height: 88px; }
  .card--back .brand__word { font-size: 62px; }
  .card--back .brand__line { font-size: 19px; padding-left: 3px; }

  .divider {
    position: absolute;
    left: 362px;
    top: 140px;
    width: 2px;
    height: 164px;
    background: var(--rule);
  }
  .details {
    position: absolute;
    left: 381px;
    top: 98px;
    list-style: none;
    color: var(--detail);
    font-size: 14.5px;
    line-height: 29px;
  }
  .details__note { font-size: 8px; }
</style>
</head>
<body>
  <section class="card card--front" aria-label="Card front">
    <div class="brand">
      <span class="brand__mark"></span>
      <span class="brand__name">
        <span class="brand__word">Corwen</span>
        <span class="brand__line">Property Management</span>
      </span>
    </div>
    <div class="divider"></div>
    <ul class="details">
      <li>Dean Fosterly - Principal</li>
      <li>Tessa Fosterly - Director <span class="details__note">(Property Management)</span></li>
      <li>PO Box 718</li>
      <li>Holloway SA 5093</li>
      <li>Dean: 0419 372 508</li>
      <li>Tessa: 0419 613 947</li>
      <li>www.corwenpropertymanagement.com.au</li>
      <li>admin@corwenpropertymanagement.com.au</li>
    </ul>
  </section>

  <section class="card card--back" aria-label="Card back">
    <div class="brand">
      <span class="brand__mark"></span>
      <span class="brand__name">
        <span class="brand__word">Corwen</span>
        <span class="brand__line">Property Management</span>
      </span>
    </div>
  </section>
</body>
</html>
```